Snapnook needs You

Help us create an inviting, amazing, sleek, simple, clear landing page for a picture-memory-social connection site!

Business Name: SnapNook
Industry: Social Networking and Creativity through Pictures
A web platform for and about a community that is driven by a passion for sharing, caring, bonding, collaborating, creating and earning with pictures, through pictures and other related creative activities. This is going to be a great site for all creative artists-photographers, artists, graphic artists to express their work and their creativity.

The main focus of the site is - CONNECTIONS.
This will be uncoded.

Desired Website Screen Size
1024x768... Widescreen/Landscape orientation, is what we mean... So it fits on a CPU screen.

Desired look and feel and message
Look: Visitor should feel immersed in the page, in the world the page creates, simple, elegant, sophisticated, contemporary. We really like a clean uncluttered look.

Special mention: By the way we love the marketing genius who thought up this branding for velu yogurt where they used the two dots above the o to create a branding effect that made this brand instantly identifiable. http://www.velu-dairy.ca/en/

The two dots by themselves without having even the name present brings up the whole brand now. The dots are used above all the ingredients of the yogurt creating friendly figures, and above people in commercials-bringing the people onto the side of "team" velu. Snapnook may have a character created or something distinctive in the letters in the name created to brand the site as well.

Feel: Engaging; Magical without being corny, here is a link to give an example look and feel but please do not be hindered in your creativity by this suggestion. We love all creative angles.
http://artscrapheap.com/graphic/5820317-camera-film-roll-blue-background

Message: Life and memories and connections through pictures.

Target audience:
The site is focused on pictures but not confined to photography enthusiasts (although they are an integral part of the site). Customers/Visitors will include families, corporates and the younger generation - all age groups, all class, everyone with pictures to express, memories to share.

Website design we like:
http://morvantstudio.com/work/northern-ballet-guild/
http://morvantstudio.com/work/pixelhop/

What colors do we want to see on our landing page?
We would like the background to be grey or blue since it is grey is picture neutral colour and blue highlights pictures well and we also like blue and silver, which can be integrated into the theme. Also like green. But please do not let these instructions limit your creativity. We are open to new ideas and colours.

Predetermined Concepts if any:
We have a concept in mind and we think it would be cool to have an interface for the user through the back of a camera on the landing page -This could be used to create a scene or world the visitor feels a part of or is immersed into. The back screen of the camera may act as a screen for the slideshow of featured pictures on the site.

Content on the Page:
Photo Gallery with full screen, thumbnail view, zoom option etc.
Prominent but short introductory message
Sign in / Login Options
Links: Home Page; About; Info/Help; Contact Us; Privacy Policy; Terms of Use
At the bottom of the page: Follow Me/Like/Workfolio...social buttons.

Please feel free to add any other element to the landing page that you think might add to the effect of simple yet amazing look -clean, simple, uncluttered, sophisticated, stylish, inviting and engaging.
The concept is a guideline, but we would like you to be as creative as you can, even if it meant stepping out of these guidelines - rethink design, style, content if you like. We believe in bringing a solution in an innovative yet simple and elegant style. Something a visitor would be intrigued enough to explore and the guest would feel comfortable enough taking that step forward to have fun on the site. If you believe in the same, and you have the skill then you will have what we need. Good luck, go for it and we are excited to see what the amazing designers on this amazing site have to offer.
If you have any questions please free to ask.
Updates

HI wanted to send an update that this project design has been guaranteed.

Our site will be one to celebrate and showcase imagination as well as connection.  We would love to see what you create. Keep in mind our site will showcase all creativity, photographs, artists, graphic artists so this would be a benefit you may want to take advantage of in the future, a place where, if you so choose, you could gain exposure for your work. Therefore, even if you do not win the design project there is possible future benefit.

Imagination is everything.
Imagination encircles the world.-Harwood

Reason: We are giving the designers who accepted invites but have not yet submitted a chance to finish their submissions and the ones who are working on revisions a chance to finish those:)

Hello everyone,

Due to time constraints we must come to a decision sooner than the deadline of 28th. 

So, please try to submit any new designs or modifications to the old ones before the 26th. We are very thankful to all of you who have participated - for your designs, enthusiasm and kind words. 

Good luck! :)

• Thank you for the interest shown and your submissions! Designers who have submitted up until now have shown great potential. We are VERY excited with the quality of work and designs.

We want to add that Snapnook is not exclusively for the photographers. The site is for every person who may have a picture to store, organise, use or share - whether publicly or with only a few friends and family.

Snapnook is about allowing people to take control of their creativity. It is about providing tools to our users so that they can build their own connections and social network... of friends, family, fans, clients, ideas, thoughts, emotions etc. through pictures without worrying about their privacy or control over their creations.

With this update we want to encourage others to go beyond the camera theme. Do not let us restrict your creativity. Let YOUR OWN ideas take over if that’s what you think will best convey the message and will appeal to the users.

```html
<!DOCTYPE html>
<html lang="en">
<head>
<meta charset="utf-8">
<title>SnapNook</title>
<link rel="stylesheet" href="https://fonts.googleapis.com/css2?family=Arimo:wght@400;700&family=Pacifico&display=swap">
<style>
:root{
  --wood-light:#f3dcae;
  --wood-mid:#e8c78c;
  --wood-dark:#d9ad6a;
  --page-grey:#f1f1f1;
  --band-blue:#1a6e96;
  --panel-navy:#123b52;
  --panel-fold:#0b2636;
  --ink:#333333;
  --white:#ffffff;
  --green:#1fa84c;
  --gold:#c99a2e;
  --footer-grey:#e6e6e6;
  --footer-ink:#4a4a4a;
}
*{box-sizing:border-box;margin:0;padding:0}
html,body{width:1200px;height:900px;overflow:hidden}
body{position:relative;background:var(--page-grey);font-family:"Arimo",Arial,sans-serif;color:var(--ink)}
.script{font-family:"Pacifico",cursive;font-weight:400}

/* header */
.site-header{position:absolute;left:0;top:0;width:1200px;height:129px;
  background:repeating-linear-gradient(90deg,rgba(255,255,255,.08) 0 3px,rgba(0,0,0,.03) 3px 7px),
  linear-gradient(180deg,var(--wood-light),var(--wood-mid));
  border-bottom:2px solid #c9a770}
.brand{position:absolute;left:54px;top:40px;display:flex;align-items:center;gap:10px;
  font-family:"Pacifico",cursive;font-size:32px;color:var(--white)}
.brand-mark{width:22px;height:22px;background:var(--white);border-radius:3px}
.main-nav{position:absolute;top:55px;left:0;font-weight:700;font-size:18px;color:var(--white)}
.main-nav a{position:absolute;color:var(--white);text-decoration:none;white-space:nowrap}
.auth-btn{position:absolute;top:53px;height:31px;border-radius:16px;
  background:linear-gradient(180deg,#ecd07a,var(--gold));border:2px solid #a87c1c;
  font-family:"Pacifico",cursive;font-size:16px;color:var(--white);text-align:center;line-height:24px}

/* hero */
.slider-frame{position:absolute;left:41px;top:159px;width:710px;height:403px;
  background:linear-gradient(180deg,var(--wood-light),var(--wood-mid));box-shadow:0 2px 4px rgba(0,0,0,.15)}
.slider-mat{position:absolute;left:23px;top:23px;width:668px;height:361px;background:var(--white);
  box-shadow:0 0 0 2px #e0c48f}
.slider-photo{position:absolute;left:20px;top:22px;width:624px;height:317px;
  background:linear-gradient(180deg,#1c2a44 0%,#3a3450 45%,#a0553a 62%,#2a2220 75%,#0e0d10 100%)}
.slider-dots{position:absolute;top:566px;left:363px;display:flex;gap:8px}
.slider-dots span{width:11px;height:11px;border-radius:50%;background:#d8d8d8;border:1px solid #9a9a9a}

.network-art{position:absolute;left:818px;top:158px;width:321px;height:217px;
  background:radial-gradient(ellipse at center,#d7e6ef 0%,#eef3f6 60%,var(--page-grey) 100%)}
.intro-title{position:absolute;left:834px;top:396px;font-size:40px;color:var(--ink);white-space:nowrap}
.intro-text{position:absolute;left:831px;top:465px;width:300px;font-size:13.5px;line-height:17.6px;color:#222}

/* blue band */
.info-band{position:absolute;left:0;top:609px;width:1200px;height:232px;background:var(--band-blue)}
.band-title{position:absolute;font-size:23px;color:var(--white);white-space:nowrap}
.about-text{position:absolute;left:61px;top:674px;width:370px;font-size:13.5px;line-height:17.6px;color:var(--white)}
.thumb{position:absolute;width:98px;height:76px;border:3px solid #d9d9d9;box-shadow:0 2px 4px rgba(0,0,0,.3)}

.newsletter{position:absolute;left:795px;top:595px;width:365px;height:184px;
  background:repeating-linear-gradient(0deg,rgba(255,255,255,.03) 0 2px,transparent 2px 8px),var(--panel-navy);
  box-shadow:0 4px 8px rgba(0,0,0,.35)}
.newsletter-fold{position:absolute;left:1160px;top:595px}
.newsletter-title{position:absolute;left:16px;top:42px;font-size:22px;color:var(--white);display:flex;align-items:center;gap:8px}
.email-field{position:absolute;left:16px;top:81px;width:230px;height:26px;background:var(--white);
  border:none;padding-left:6px;font-family:"Arimo",Arial,sans-serif;font-size:13px;color:#888}
.submit-btn{position:absolute;left:256px;top:80px;width:87px;height:28px;border-radius:14px;
  background:linear-gradient(180deg,#39c266,var(--green));border:1px solid #0d7a32;
  font-family:"Pacifico",cursive;font-size:15px;color:var(--white);line-height:24px;text-align:center}
.newsletter-note{position:absolute;left:16px;top:120px;width:340px;font-size:12.5px;line-height:16px;color:var(--white)}

/* footer */
.site-footer{position:absolute;left:0;top:841px;width:1200px;height:59px;
  background:repeating-linear-gradient(45deg,#ececec 0 2px,var(--footer-grey) 2px 4px);font-size:11.5px;color:var(--footer-ink)}
.site-footer span{position:absolute;top:25px;white-space:nowrap}
.social-dot{position:absolute;top:11px;width:36px;height:36px;border-radius:50%;
  background:linear-gradient(180deg,#3c7fb0,#1d5580);box-shadow:0 1px 2px rgba(0,0,0,.3)}
</style>
</head>
<body>

<header class="site-header">
  <div class="brand"><span class="brand-mark"></span>SnapNook</div>
  <nav class="main-nav">
    <a style="left:390px">Home</a>
    <a style="left:484px">About Us</a>
    <a style="left:612px">Info</a>
    <a style="left:694px">Contact Us</a>
  </nav>
  <div class="auth-btn" style="left:824px;width:87px">Log in</div>
  <div class="auth-btn" style="left:928px;width:89px">Sign Up</div>
</header>

<section class="slider-frame">
  <div class="slider-mat">
    <div class="slider-photo" role="img" aria-label="Featured photograph: a lit bridge with twin towers over a river at dusk"></div>
  </div>
</section>
<div class="slider-dots"><span></span><span></span><span></span><span></span></div>

<div class="network-art" role="img" aria-label="Illustration of colourful picture tiles linked together in a network"></div>
<h1 class="intro-title script">Get Connected</h1>
<p class="intro-text">Lorem ipsum dolor sit amet, consectetur adipiscing elit. Aliquam accumsan sagittis velit. Fusce a augue nisl. Cras scelerisque porttitor arcu, at malesuada nulla rutrum sed. Curabitur quis massa massa, at auctor nunc. Phasellus pellentesque aliquam libero vel tincidunt. Integer id dolor id elit elementum rhoncus.</p>

<section class="info-band"></section>
<h2 class="band-title script" style="left:61px;top:625px">About SnapNook</h2>
<p class="about-text">Lorem ipsum dolor sit amet, consectetur adipiscing elit. Aliquam accumsan sagittis velit. Fusce a augue nisl. Cras scelerisque porttitor arcu, at malesuada nulla rutrum sed. Curabitur quis massa massa, at auctor nunc. Phasellus pellentesque aliquam libero vel tincidunt. Integer id dolor id elit elementum rhoncus.</p>

<h2 class="band-title script" style="left:444px;top:625px">Featured Images</h2>
<div class="thumb" style="left:444px;top:664px;background:linear-gradient(135deg,#444,#111)" role="img" aria-label="Hands holding a small globe"></div>
<div class="thumb" style="left:560px;top:664px;background:linear-gradient(135deg,#3bb56a,#1f8a48)" role="img" aria-label="Green artwork thumbnail"></div>
<div class="thumb" style="left:676px;top:664px;background:linear-gradient(180deg,#9cc3e0,#d8c7a4)" role="img" aria-label="Person sitting on a beach"></div>
<div class="thumb" style="left:444px;top:752px;background:linear-gradient(135deg,#c8cf8a,#6f7a3a)" role="img" aria-label="Stack of green biscuits"></div>
<div class="thumb" style="left:560px;top:752px;background:linear-gradient(135deg,#d9b27a,#7a4e22)" role="img" aria-label="Close-up of a cookie"></div>
<div class="thumb" style="left:676px;top:752px;background:linear-gradient(135deg,#444,#111)" role="img" aria-label="Hands holding a small globe"></div>

<aside class="newsletter">
  <h2 class="newsletter-title script">Newsletter
    <svg width="24" height="20" viewBox="0 0 24 20" aria-hidden="true"><path d="M2 8 L12 1 L22 8 V19 H2 Z" fill="#3aa0d8"/><path d="M2 8 L12 14 L22 8" fill="none" stroke="#123b52" stroke-width="2"/></svg>
  </h2>
  <input class="email-field" type="text" value="Email" readonly>
  <div class="submit-btn">Submit</div>
  <p class="newsletter-note">Sign up to our newsletter and be the first to know about our updates, competitions and much more!</p>
</aside>
<svg class="newsletter-fold" width="28" height="14" viewBox="0 0 28 14" aria-hidden="true" style="top:595px"><path d="M0 0 H14 L28 14 H0 Z" fill="var(--panel-fold)"/></svg>

<footer class="site-footer">
  <span style="left:30px">© 2012 SnapNook All Rights Reserved</span>
  <span style="left:292px">Privacy Policy</span>
  <span style="left:379px">Terms &amp; Conditions</span>
  <div class="social-dot" style="left:1008px" role="img" aria-label="Social link"></div>
  <div class="social-dot" style="left:1051px" role="img" aria-label="Social link"></div>
  <div class="social-dot" style="left:1094px" role="img" aria-label="Social link"></div>
  <div class="social-dot" style="left:1138px" role="img" aria-label="Social link"></div>
</footer>

</body>
</html>
```